I need a website for my moving company Brisk Haulers LLC. I would like the following text included in my website. I have purchased the domain briskhaulersco.example from nametrellis.example. I am not familiar with SEO or other techniques that help my page on search engines but would like the website to be optimized for Scoutly search engine. I have attached our logo below and would like it to be used in the design. The colors in the logo can be used also in the design.
Home/About Us
At Brisk Haulers LLC, we know moving. It can be difficult, stressful, and a real pain in the backside. But it doesn’t have to be! When you partner with Brisk, you get the benefits of a professional moving team that is licensed and insured for your protection along with years of experience and a dedication to providing the highest quality service, each and every time.
Our Services
We do a wide variety of local moves, including apartments, single-family homes, retirement communities, dorms, condos, and many more! Our movers are trained to protect your belongings and your home – all pieces of furniture are padded and stretch wrapped free of charge, ensuring your items and home are damage-free at the end of your move. Having added stress about packing up your home prior to moving? We’ve got you covered with our full service packing and unpacking services, too.
What You Get
When you partner with BRISK, you’ll get the best service in the industry, as well as:
* The Use of Packing & Moving Materials: The hourly rate includes the use of our dollies, ratchet straps, pads, moving tools, and property protection like floor mats, door-jamb protectors, stairwell protectors, and plenty of muscle!
• Trained, Licensed, and Insured Movers: All of our movers are highly trained to provide you with the best service, and to ensure the protection of you and your items.
• Professional: Honest, Uniformed, Nice, Knowledgeable Service is what you’ll get with every member of our moving teams.
• Custom Service for Every Move: Every move is as unique as the person or business moving. Our training and equipment allows us to customize every project to ensure the very best for every client.
Target Market(s)
Home and Business movers
Industry/Entity Type
Moving Company
Colors
Designer to choose colors to be used in the design.
Requirements
Must have
- 2 sides
Nice to have
- Colorful design with logo included.
Should not have
- animated characters

```html
<!DOCTYPE html>
<html lang="en">
<head>
<meta charset="utf-8">
<title>Brisk Moving</title>
<link rel="stylesheet" href="https://fonts.googleapis.com/css2?family=Domine:wght@400;700&family=Lato:wght@400;700&display=swap">
<style>
:root{
  --orange:#f7941d;
  --green:#8cc63f;
  --green-dark:#6fa92b;
  --ink:#1c1c1c;
  --text:#555;
  --muted:#f4f4f4;
  --white:#fff;
  --serif:'Domine', Georgia, serif;
  --sans:'Lato', Arial, sans-serif;
}
*{box-sizing:border-box;margin:0;padding:0}
html,body{width:1200px;height:3516px;overflow:hidden}
body{font-family:var(--sans);color:var(--text);background:var(--white);position:relative}
section,header,footer{position:relative;width:1200px}

/* header + hero */
.hero{height:645px;background:linear-gradient(100deg,#8a7660 0%,#6b5a48 35%,#3e3a36 60%,#5b5751 100%)}
.hero-photo{position:absolute;inset:0}
.hero::after{content:"";position:absolute;inset:0;background:rgba(0,0,0,.28)}
.topbar{position:absolute;top:0;left:0;width:1200px;height:103px;background:rgba(15,15,15,.82);z-index:3;border-bottom:1px solid rgba(255,255,255,.15)}
.nav a{position:absolute;top:43px;color:var(--white);font-size:16px;text-decoration:none}
.brand{position:absolute;display:flex;align-items:center;font-family:var(--sans);font-weight:700;color:var(--orange);flex-direction:column;gap:4px;font-size:19px;white-space:nowrap}
.topbar .brand{left:554px;top:22px}
.brand-mark{width:30px;height:30px;background:var(--green);border-radius:3px}
.search{position:absolute;left:1074px;top:38px}
.hang{position:absolute;left:234px;top:103px;width:2px;height:112px;background:var(--orange);z-index:3}
.hang-dot{position:absolute;left:228px;top:208px;width:14px;height:14px;border-radius:50%;border:2px solid var(--orange);background:#111;z-index:4}
.quote-form{position:absolute;left:84px;top:228px;width:300px;height:300px;border-radius:50%;background:#0e0e0e;border:3px solid var(--orange);z-index:3;text-align:center;padding-top:36px}
.quote-form h3{color:var(--orange);font-size:18px;font-weight:400;margin-bottom:10px}
.quote-form .field{width:210px;height:40px;margin:0 auto 12px;background:var(--white);text-align:left;padding:10px 12px;font-size:13px;color:#555}
.quote-form .btn{display:inline-block;width:104px;height:38px;line-height:38px;background:var(--green);color:var(--white);font-size:16px}
.hero-copy{position:absolute;left:530px;top:338px;width:580px;z-index:3;color:var(--white);text-align:center;font-size:20px;line-height:31px}
.hero-copy em{font-style:normal;color:var(--orange)}
.dots{position:absolute;display:flex;gap:6px;z-index:3}
.dots i{width:14px;height:14px;border:1.5px solid #bbb;background:rgba(255,255,255,.2)}
.dots i.on{background:var(--orange);border-color:var(--orange)}
.hero .dots{left:570px;top:583px}

/* headings */
.sec-title{display:flex;justify-content:center;align-items:center;gap:12px;font-family:var(--serif);font-weight:400;color:var(--orange);font-size:38px}
.sec-title .brand-mark{width:34px;height:26px;background:var(--orange)}
.sec-title span.g{color:var(--green)}

/* welcome */
.welcome{height:363px;background:var(--muted);padding-top:62px;text-align:center}
.welcome p{width:710px;margin:28px auto 0;font-size:14px;line-height:27px;color:#555}
.btn-green{display:inline-block;background:var(--green);color:var(--white);font-size:18px;text-align:center}
.welcome .btn-green{width:164px;height:52px;line-height:52px;margin-top:30px}

/* services */
.services{height:996px;padding-top:62px}
.service{position:absolute;width:312px;height:365px;border:1px solid #ddd;background:var(--white);text-align:center}
.service .photo{height:187px}
.service .badge{position:absolute;left:116px;top:146px;width:80px;height:80px;border-radius:50%;background:#111;border:4px solid var(--orange);display:flex;align-items:center;justify-content:center}
.service h3{margin-top:64px;font-family:var(--serif);font-weight:400;font-size:24px;color:var(--green)}
.service p{width:262px;margin:8px auto 0;font-size:13.5px;line-height:21.5px;color:#666}

/* testimonial */
.testimonial{height:469px;background:linear-gradient(90deg,#3a3430,#4b4440 40%,#5a544c 70%,#2e2b28);text-align:center;padding-top:58px;color:var(--white)}
.testimonial::before{content:"";position:absolute;inset:0;background:rgba(0,0,0,.45)}
.testimonial > *{position:relative}
.testimonial .sec-title{color:var(--green)}
.avatar{width:116px;height:116px;border-radius:50%;background:linear-gradient(#d8c0ac,#9c7f6c);border:4px solid var(--white);margin:22px auto 0}
.testimonial p{width:740px;margin:26px auto 0;font-size:14px;line-height:25px}
.testimonial .name{margin-top:12px;color:var(--orange);font-size:15px}
.testimonial .role{font-size:13px;margin-top:2px}
.testimonial > .dots{position:absolute;left:570px;top:390px}

/* contact */
.contact{height:574px;padding-top:52px}
.contact .field{position:absolute;left:77px;width:582px;background:var(--orange);border-radius:4px;color:var(--white);font-size:15px;padding:18px 16px}
.contact .btn-green{position:absolute;left:204px;top:454px;width:361px;height:61px;line-height:61px;border-radius:3px;font-size:21px}
.contact .photo{position:absolute;left:668px;top:105px;width:532px;height:469px;background:radial-gradient(circle at 72% 30%,#d9d2c4,#f4f0ea 45%,#fff 70%)}

/* footer */
.site-footer{height:394px;background:linear-gradient(90deg,#1d1b19,#2d2925 50%,#1a1816);color:#ddd;font-size:13.5px;line-height:26px}
.site-footer::before{content:"";position:absolute;inset:0;background:rgba(0,0,0,.35)}
.site-footer > *{position:absolute}
.site-footer > h4{top:72px;font-family:var(--serif);font-weight:400;color:var(--orange);font-size:18px;line-height:26px}
.site-footer > .brand{left:150px;top:56px}
.site-footer > .about-col{left:80px;top:145px;width:240px}
.site-footer > .contact-list{left:389px;top:110px}
.contact-list li{list-style:none;display:flex;gap:14px;align-items:flex-start;margin-bottom:8px}
.contact-list li svg{margin-top:4px;flex:none}
.contact-list li b{color:var(--orange);font-weight:400}
.site-footer > .news{left:633px;top:105px;width:250px}
.news .input{width:250px;height:42px;background:#eee;margin-top:10px;color:#555;padding:8px 10px}
.news .btn{width:156px;height:46px;line-height:46px;margin-top:12px;background:var(--orange);color:var(--white);text-align:center;font-size:18px}
.site-footer > .thumb{width:94px;height:94px;border:2px solid var(--white)}
.bottombar{height:75px;background:var(--orange);color:var(--white);font-size:14px}
.bottombar .copy{position:absolute;left:80px;top:28px}
.bottombar nav{position:absolute;right:80px;top:28px;display:flex;gap:12px}
.bottombar nav span{opacity:.8}
</style>
</head>
<body>

<header class="hero">
  <div class="hero-photo" role="img" aria-label="Couple sitting among moving boxes in a new home"></div>
  <div class="topbar">
    <nav class="nav">
      <a style="left:190px">Home</a>
      <a style="left:295px">About us</a>
      <a style="left:403px">Our Services</a>
      <a style="left:689px">What You Get</a>
      <a style="left:839px">News</a>
      <a style="left:928px">Contact us</a>
    </nav>
    <div class="brand"><span class="brand-mark"></span>BRISK MOVING</div>
    <svg class="search" width="26" height="26" viewBox="0 0 26 26" fill="none" stroke="#8cc63f" stroke-width="2.5"><circle cx="11" cy="11" r="8"/><path d="M17 17l7 7"/></svg>
  </div>
  <div class="hang"></div>
  <div class="hang-dot"></div>
  <form class="quote-form">
    <h3>BRISK MOVING</h3>
    <div class="field">Name :</div>
    <div class="field">Phone :</div>
    <div class="field">Address :</div>
    <span class="btn">SEND</span>
  </form>
  <p class="hero-copy">When it's time to move out of your home or business.It's time to call <em>BRISKMOVING</em>.We make it easy on you and faster than the other.</p>
  <div class="dots"><i></i><i class="on"></i><i></i></div>
</header>

<section class="welcome">
  <h2 class="sec-title"><span class="brand-mark"></span>Welcome to BRISK MOVING</h2>
  <p>Lorem Ipsum is simply dummy text of the printing and typesetting industry. Lorem Ipsum has been the industry's standard dummy text ever since the 1500s, when an unknown printer took a galley of type and scrambled it to make a type specimen book. It has survived not only five centuries, but also the leap into electronic typesetting, remaining essentially unchanged.</p>
  <span class="btn-green">READ MORE</span>
</section>

<section class="services">
  <h2 class="sec-title"><span class="brand-mark"></span>Our SERVICES</h2>

  <article class="service" style="left:77px;top:140px">
    <div class="photo" role="img" aria-label="Family unpacking boxes on a sofa" style="background:linear-gradient(#e9e3dc,#c9b8a4)"></div>
    <div class="badge"><svg width="40" height="40" viewBox="0 0 40 40" fill="#8cc63f"><rect x="4" y="18" width="14" height="14"/><rect x="20" y="24" width="10" height="8"/><circle cx="30" cy="10" r="4"/><rect x="27" y="15" width="6" height="9"/></svg></div>
    <h3>local moves</h3>
    <p>Lorem Ipsum is simply dummy text of the printing and typesetting industry. Lorem Ipsum has been typing...(+)</p>
  </article>
  <article class="service" style="left:443px;top:140px">
    <div class="photo" role="img" aria-label="Couple in a bright apartment" style="background:linear-gradient(#efece6,#b9ad9c)"></div>
    <div class="badge"><svg width="40" height="40" viewBox="0 0 40 40" fill="#8cc63f"><rect x="6" y="10" width="12" height="24"/><rect x="20" y="4" width="14" height="30"/></svg></div>
    <h3>Including apartments</h3>
    <p>Lorem Ipsum is simply dummy text of the printing and typesetting industry. Lorem Ipsum has been typing...(+)</p>
  </article>
  <article class="service" style="left:811px;top:140px">
    <div class="photo" role="img" aria-label="Single-family house lit at dusk" style="background:linear-gradient(#2b3340,#4a4034)"></div>
    <div class="badge"><svg width="40" height="40" viewBox="0 0 40 40" fill="#8cc63f"><path d="M20 5L4 19h5v15h22V19h5z"/></svg></div>
    <h3>Single-family homes</h3>
    <p>Lorem Ipsum is simply dummy text of the printing and typesetting industry. Lorem Ipsum has been typing...(+)</p>
  </article>

  <article class="service" style="left:77px;top:567px">
    <div class="photo" role="img" aria-label="Senior couple in a living room" style="background:linear-gradient(#ddd2c4,#a89380)"></div>
    <div class="badge"><svg width="40" height="40" viewBox="0 0 40 40" fill="#8cc63f"><path d="M20 5L4 19h5v15h22V19h5z"/></svg></div>
    <h3>Retirement communities</h3>
    <p>Lorem Ipsum is simply dummy text of the printing and typesetting industry. Lorem Ipsum has been typing...(+)</p>
  </article>
  <article class="service" style="left:443px;top:567px">
    <div class="photo" role="img" aria-label="Movers carrying a sofa outdoors" style="background:linear-gradient(#8fa26b,#c9b59b)"></div>
    <div class="badge"><svg width="40" height="40" viewBox="0 0 40 40" fill="#8cc63f"><rect x="6" y="6" width="4" height="28"/><rect x="30" y="6" width="4" height="28"/><rect x="10" y="12" width="20" height="5"/><rect x="10" y="24" width="20" height="5"/></svg></div>
    <h3>Dorms</h3>
    <p>Lorem Ipsum is simply dummy text of the printing and typesetting industry. Lorem Ipsum has been typing...(+)</p>
  </article>
  <article class="service" style="left:811px;top:567px">
    <div class="photo" role="img" aria-label="Uniformed movers with boxes" style="background:linear-gradient(#cfd6de,#8e9aa8)"></div>
    <div class="badge"><svg width="40" height="40" viewBox="0 0 40 40" fill="#8cc63f"><rect x="6" y="18" width="8" height="16"/><rect x="16" y="10" width="8" height="24"/><rect x="26" y="4" width="8" height="30"/></svg></div>
    <h3>Condos</h3>
    <p>Lorem Ipsum is simply dummy text of the printing and typesetting industry. Lorem Ipsum has been typing...(+)</p>
  </article>
</section>

<section class="testimonial" role="img" aria-label="Family carrying boxes in front of a home">
  <h2 class="sec-title"><span class="brand-mark"></span><span class="g">What Our Client Say</span></h2>
  <div class="avatar" role="img" aria-label="Client portrait"></div>
  <p>Lorem Ipsum is simply dummy text of the printing and typesetting industry. Lorem Ipsum has been the industry's standard dummy text ever since the 1500s.</p>
  <div class="name">DANA MORROW</div>
  <div class="role">Manager, Brisk Haulers LLC</div>
  <div class="dots"><i></i><i class="on"></i><i></i></div>
</section>

<section class="contact">
  <h2 class="sec-title"><span class="brand-mark"></span>Contact Us</h2>
  <div class="field" style="top:131px;height:61px">Name* :</div>
  <div class="field" style="top:204px;height:61px">Phone* :</div>
  <div class="field" style="top:276px;height:61px">Address* :</div>
  <div class="field" style="top:351px;height:89px">Comment :</div>
  <span class="btn-green">SEND REQUEST</span>
  <div class="photo" role="img" aria-label="Mover holding boxes beside a globe and parcels"></div>
</section>

<footer class="site-footer" role="img" aria-label="Moving truck loaded with boxes">
  <div class="brand"><span class="brand-mark"></span>BRISK MOVING</div>
  <p class="about-col">Lorem Ipsum is simply dummy text of the printing and typesetting industry<br>Lorem Ipsum is simply dummy text of the printing and typesetting industry</p>

  <h4 style="left:389px">Quick Link</h4>
  <ul class="contact-list">
    <li><svg width="16" height="20" viewBox="0 0 16 20" fill="#f7941d"><path d="M8 0a7 7 0 0 0-7 7c0 5 7 13 7 13s7-8 7-13a7 7 0 0 0-7-7zm0 10a3 3 0 1 1 0-6 3 3 0 0 1 0 6z"/></svg><span><b>BRISK MOVING</b><br>United States</span></li>
    <li><svg width="18" height="18" viewBox="0 0 18 18" fill="#f7941d"><path d="M4 1l3 4-2 2a10 10 0 0 0 6 6l2-2 4 3-2 3C8 17 1 10 1 3z"/></svg><span>(555) 014-2290</span></li>
    <li><svg width="18" height="14" viewBox="0 0 18 14" fill="#f7941d"><rect width="18" height="14" rx="1"/><path d="M1 1l8 7 8-7" stroke="#222" stroke-width="1.5" fill="none"/></svg><span>support@briskhaulers.example</span></li>
  </ul>

  <h4 style="left:633px">Newsletter</h4>
  <div class="news">
    <p style="margin-top:14px;line-height:23px">Would you like to receive exclusive access to articles, white papers and our regular monthly newsletter?</p>
    <div class="input">Enter Email Id</div>
    <div class="btn">SUBSCRIBE</div>
  </div>

  <h4 style="left:919px">Latest Blog</h4>
  <div class="thumb" style="left:919px;top:117px;background:linear-gradient(#d9e4ee,#8aa0b6)" role="img" aria-label="Blog photo of movers"></div>
  <div class="thumb" style="left:1027px;top:117px;background:linear-gradient(#eee6da,#b8a58e)" role="img" aria-label="Blog photo of packing"></div>
  <div class="thumb" style="left:919px;top:227px;background:linear-gradient(#cdd9e6,#6d8299)" role="img" aria-label="Blog photo of a moving team"></div>
  <div class="thumb" style="left:1027px;top:227px;background:linear-gradient(#e8e2d8,#9c8a78)" role="img" aria-label="Blog photo of boxes"></div>
</footer>

<section class="bottombar">
  <div class="copy">BRISK MOVING | Copyright - 2017.All Rights Reserved</div>
  <nav><span>Home</span><span>|</span><span>About</span><span>|</span><span>Our Services</span><span>|</span><span>What You Get</span><span>|</span><span>Contact</span></nav>
</section>

</body>
</html>
```